QTR tub packaging design

Hi!
We require a design for two different flavours of packaging for a protein recovery formula.
The design will be for the cardboard tubs as in pic attached. The name of the product will be 'LW recovery formula'. The LW logo is also attached and can be slightly adjusted.
The project will require a design for the front and then a basic design for the information on the back. This will include ingredients, nutrition info, directions and production location. On the back it will also need the 'lift your stride' logo and something referring to 'LW recovery formula by 'Your Vital Ember' (logo for this is attached).
The product will come in two flavours (cacao and coconut, then vanilla and acai) so will need the basic design adjusted for each flavour. The tubs are 1kg and this will need to be somewhere on the front of the tub.
This product is designed for healthy and active people, mainly female focused. The design should be clean and not overloaded with colours and pictures. It should only be two colours max. The final design should communicate that the product will assist people to reach their goals, whilst being health focused.

Target Market(s)

Active Females 20-50

Industry/Entity Type

Nutrition

Requirements
Must have
• Nutrition information and ingredients area
• Three logos attached
• Name- recovery formula
Should not have
• Not too busy, too many pictures or information. Please keep it simple.

```html
<!DOCTYPE html>
<html lang="en">
<head>
<meta charset="utf-8">
<title>LW Recovery Formula – Coconut &amp; Cacao tub wrap</title>
<link rel="stylesheet" href="https://fonts.googleapis.com/css2?family=Archivo+Black&family=Barlow:wght@400;700&family=Great+Vibes&display=swap">
<style>
  :root {
    --bg: #ffffff;
    --kraft: #bb9f7c;
    --kraft-edge: #a88b67;
    --brown: #4a2418;
    --green: #8cc63f;
    --seam: #a3865f;
  }
  * { box-sizing: border-box; margin: 0; padding: 0; }
  html, body { width: 1200px; height: 1200px; overflow: hidden; background: var(--bg); }
  .canvas { position: relative; width: 1200px; height: 1200px; }

  .wrap {
    position: absolute; left: 250px; top: 90px; width: 700px; height: 1020px;
    background: var(--kraft); border: 2px solid var(--kraft-edge);
  }
  .lid-seam { position: absolute; left: 0; right: 0; top: 300px; height: 3px; background: var(--seam); }

  /* product lockup (lid and front share structure) */
  .lockup { position: absolute; }
  .lockup .product-mark {
    font-family: "Archivo Black", sans-serif; color: var(--brown); line-height: .85; letter-spacing: 2px;
  }
  .lockup .product-name {
    font-family: "Archivo Black", sans-serif; color: var(--green); line-height: 1.05; letter-spacing: 4px;
    text-transform: uppercase;
  }
  .lockup .flavour {
    position: absolute; font-family: "Great Vibes", cursive; color: var(--brown); line-height: .9;
  }
  .lockup .flavour .amp { color: var(--green); }
  .lockup .flavour-art {
    position: absolute; border-radius: 40% 50% 45% 50%;
    background: linear-gradient(90deg, #ffffff 0%, #f3ece0 30%, #5b2d1d 55%, var(--brown) 100%);
  }
  .lockup .weight {
    position: absolute; font-family: "Archivo Black", sans-serif; color: var(--green);
  }

  .lid-lockup { left: 110px; top: 50px; width: 480px; height: 150px; }
  .lid-lockup .product-mark { font-size: 64px; }
  .lid-lockup .product-name { font-size: 22px; }
  .lid-lockup .flavour { left: 250px; top: 0; font-size: 34px; }
  .lid-lockup .flavour-art { left: 250px; top: 62px; width: 170px; height: 52px; }
  .lid-lockup .weight { left: 330px; top: 118px; font-size: 20px; }

  .brand {
    position: absolute; left: 0; right: 0; top: 200px; text-align: center;
    font-family: "Barlow", sans-serif; font-weight: 700; color: var(--brown);
  }
  .brand .brand-name { font-size: 76px; line-height: 1; letter-spacing: 2px; }
  .brand .brand-full { font-size: 20px; line-height: 1.2; }

  .tagline-badge {
    position: absolute; left: 255px; top: 370px; width: 190px; height: 190px; border-radius: 50%;
    background: var(--green); display: flex; align-items: center; justify-content: center; text-align: center;
    font-family: "Barlow", sans-serif; font-weight: 400; font-size: 24px; letter-spacing: 2px; line-height: 1.2;
    color: var(--brown); text-transform: uppercase;
  }

  .front-lockup { left: 90px; top: 590px; width: 540px; height: 380px; }
  .front-lockup .product-mark { font-size: 150px; }
  .front-lockup .product-name { font-size: 36px; margin-top: 18px; }
  .front-lockup .flavour { left: 300px; top: -10px; font-size: 66px; }
  .front-lockup .flavour-art { left: 300px; top: 130px; width: 230px; height: 100px; }
  .front-lockup .weight { left: 370px; top: 240px; font-size: 30px; }
</style>
</head>
<body>
<main class="canvas">
  <section class="wrap">
    <div class="lockup lid-lockup">
      <div class="product-mark">LW</div>
      <div class="product-name">Recovery<br>Formula</div>
      <div class="flavour">Coconut <span class="amp">&amp; Cacao</span></div>
      <div class="flavour-art" role="img" aria-label="Illustration of an open coconut and cacao pods"></div>
      <div class="weight">1KG</div>
    </div>

    <div class="lid-seam"></div>

    <div class="brand">
      <div class="brand-name">QTR</div>
      <div class="brand-full">Your Vital Ember</div>
    </div>

    <div class="tagline-badge">Lift<br>your stride</div>

    <div class="lockup front-lockup">
      <div class="product-mark">LW</div>
      <div class="product-name">Recovery<br>Formula</div>
      <div class="flavour">Coconut<br><span class="amp">&amp; Cacao</span></div>
      <div class="flavour-art" role="img" aria-label="Illustration of an open coconut with milk and cacao pods"></div>
      <div class="weight">1KG</div>
    </div>
  </section>
</main>
</body>
</html>
```